24Std Betreuung Flyer Senioren
Zielgruppe
Wir vermitteln Ihnen Pflegekräfte aus Polen in 24h Betreuung. Zu diesem Zweck arbeiten wir mit unseren Partnerunternehmen in Polen und Litauen, welche ihre Pflegekraft im Rahmen der EU Dienstleistungsfreiheit legal nach Deutschland vermitteln. Das von uns vermittelte Personal ist freundlich und gut ausgebildet und verfügt über ausreichende bis gute Deutschkenntnisse. Unsere Agentur übernimmt die Koordinierung und Klärung aller Angelegenheiten für die An- und Abreise ihrer Pflegekraft. Das Personal wohnt mit der pflegebürftigen Person zusammen, wodurch wir eine 24h Betreuung realisieren können.
Aufgabenstellung
Seniorengerecht und nicht zu modern, übersichtlich nicht zu klein geschrieben evtl mit lizenzfreien Bildern von Senioren
Format: 6 seitig Wickelfalz
Informationen auf ww.altershilfe-plus.de

```html
<!DOCTYPE html>
<html lang="de">
<head>
<meta charset="utf-8">
<title>Altershilfe-Plus – 24h Betreuung</title>
<link rel="stylesheet" href="https://fonts.googleapis.com/css2?family=Arimo:wght@400;700&display=swap">
<style>
:root{
  --blue:#0580bd;
  --navy:#0c4f94;
  --light:#71b9e6;
  --mid:#2a9ad2;
  --dark:#0a6aae;
  --white:#ffffff;
  --grey:#555c63;
}
*{box-sizing:border-box;margin:0;padding:0}
html,body{width:1200px;height:848px;overflow:hidden;background:var(--white)}
body{font-family:"Arimo",Arial,sans-serif;position:relative}
.flyer{position:relative;width:1200px;height:848px;overflow:hidden}

/* left panel */
.services{position:absolute;left:0;top:0;width:390px;height:404px;background:var(--blue);color:var(--white);padding:35px 0 0 41px}
.services h2{font-size:14.5px;font-weight:700;margin-bottom:10px}
.services ul{list-style:none}
.services li{position:relative;font-size:14.6px;line-height:30px;padding-left:22px}
.services li.wrap{line-height:24px;padding-top:3px}
.services li svg{position:absolute;left:3px;top:11px;width:9px;height:8px}
.services li.wrap svg{top:11px}
.rule-left{position:absolute;left:0;top:408px;width:390px;height:6px;background:var(--blue)}
.photo{position:absolute}
.photo-exercise{left:0;top:428px;width:390px;height:420px;background:linear-gradient(135deg,#f1ece6 0%,#e2d3c4 45%,#f4f4f2 100%)}

/* middle panel */
.photo-care{left:390px;top:0;width:407px;height:258px;background:linear-gradient(120deg,#e8ddd2 0%,#efe7dc 50%,#e7ecdf 100%)}
.band{position:absolute;left:390px;top:263px;width:810px;height:13px;background:var(--blue)}
.quote{position:absolute;left:390px;top:358px;width:407px;text-align:center;color:var(--navy)}
.quote p{font-size:16.5px;font-weight:700;line-height:24.5px}
.quote cite{display:block;font-style:normal;color:var(--grey);font-size:12.5px;letter-spacing:3.6px;margin-top:5px}
.stripe{position:absolute;left:390px;width:407px}
.stripe-1{top:550px;height:21px;background:var(--light)}
.stripe-2{top:577px;height:13px;background:var(--mid)}
.stripe-3{top:596px;height:8px;background:var(--dark)}
.contact{position:absolute;left:390px;top:608px;width:407px;height:240px;background:var(--blue);color:var(--white);text-align:center;padding-top:33px;font-size:15px;line-height:24.5px}
.contact strong{font-weight:700}

/* right panel */
.brand{position:absolute;left:797px;top:0;width:403px;height:263px;display:flex;align-items:center;justify-content:center;gap:12px}
.brand-dot{width:30px;height:30px;border-radius:50%;background:var(--navy)}
.brand-name{font-size:32px;font-weight:400;color:var(--navy)}
.headline{position:absolute;left:797px;top:276px;width:403px;height:119px;background:linear-gradient(90deg,#f6f0e6,#eef2f1);color:var(--navy);padding:30px 0 0 71px}
.headline span{display:block;font-size:22px}
.headline strong{display:block;font-size:32px;font-weight:700;margin-top:4px}
.photo-hands{left:797px;top:395px;width:403px;height:453px;background:linear-gradient(160deg,#e9eddc 0%,#d9c0ad 45%,#8a4a2e 75%,#e6ecd8 100%)}
</style>
</head>
<body>
<main class="flyer">
  <section class="services">
    <h2>Unsere Dienstleistungen</h2>
    <ul>
      <li><svg viewBox="0 0 9 8"><path d="M1 4l2.5 2.5L8 1.5" fill="none" stroke="#fff" stroke-width="1.8"/></svg>legales Pflegepersonal&nbsp; (A1-Bescheinigung)</li>
      <li><svg viewBox="0 0 9 8"><path d="M1 4l2.5 2.5L8 1.5" fill="none" stroke="#fff" stroke-width="1.8"/></svg>bezahlbare Alternative zum Pflegeheim</li>
      <li><svg viewBox="0 0 9 8"><path d="M1 4l2.5 2.5L8 1.5" fill="none" stroke="#fff" stroke-width="1.8"/></svg>mehrere Kooperationspartner aus Osteuropa</li>
      <li><svg viewBox="0 0 9 8"><path d="M1 4l2.5 2.5L8 1.5" fill="none" stroke="#fff" stroke-width="1.8"/></svg>deutschsprachige Betreuer/ innen</li>
      <li><svg viewBox="0 0 9 8"><path d="M1 4l2.5 2.5L8 1.5" fill="none" stroke="#fff" stroke-width="1.8"/></svg>langjährige Erfahrung</li>
      <li><svg viewBox="0 0 9 8"><path d="M1 4l2.5 2.5L8 1.5" fill="none" stroke="#fff" stroke-width="1.8"/></svg>kostenfreier Besichtigungstermin</li>
      <li><svg viewBox="0 0 9 8"><path d="M1 4l2.5 2.5L8 1.5" fill="none" stroke="#fff" stroke-width="1.8"/></svg>zielgerichtete Beratung vor Ort</li>
      <li><svg viewBox="0 0 9 8"><path d="M1 4l2.5 2.5L8 1.5" fill="none" stroke="#fff" stroke-width="1.8"/></svg>individuelles und unverbindliches Angebot</li>
      <li class="wrap"><svg viewBox="0 0 9 8"><path d="M1 4l2.5 2.5L8 1.5" fill="none" stroke="#fff" stroke-width="1.8"/></svg>Koordination und Organisation der gesamten Auftragsabwicklung</li>
    </ul>
  </section>
  <div class="rule-left"></div>
  <div class="photo photo-exercise" role="img" aria-label="Foto: Pflegerin übt mit einem älteren Herrn mit Hanteln"></div>

  <div class="photo photo-care" role="img" aria-label="Foto: Pflegerin hält die Hand einer älteren Dame mit Gehstock"></div>
  <div class="band"></div>
  <blockquote class="quote">
    <p>”Es geht nicht darum, dem Leben<br>mehr Tage zu geben, sondern den<br>Tagen mehr Leben zu geben.“</p>
    <cite>KONRAD VELLMER</cite>
  </blockquote>
  <div class="stripe stripe-1"></div>
  <div class="stripe stripe-2"></div>
  <div class="stripe stripe-3"></div>
  <address class="contact" style="font-style:normal">
    <strong>Altershilfe-Plus</strong><br>
    Geschäftsführer: Jens Karwitz<br>
    www.altershilfe-plus.de<br>
    Email: j.karwitz@altershilfe-plus.de<br>
    Tel. 0176 418 52 607<br>
    Festnetz: 02134 907731<br>
    Fax: 02134 907732
  </address>

  <div class="brand">
    <span class="brand-dot"></span>
    <span class="brand-name">Altershilfe-Plus</span>
  </div>
  <div class="headline">
    <span>Wir kümmern uns um</span>
    <strong>Ihre Bedürfnisse</strong>
  </div>
  <div class="photo photo-hands" role="img" aria-label="Foto: ältere Hände auf einem hölzernen Gehstock"></div>
</main>
</body>
</html>
```